Gilt Corner Shop Sign

Name of company
Gilt Corner
Gilt Corner is a picture framing shop and art gallery selling custom frames, art work and gifts.
Needing a design for shop front sign.

The Sign
The sign is above the shop front window and is approximately 12 feet wide by 43 inches high. White on black. White striped boarder that looks like a picture frame with Gilt Corner in classic lettering including space for a phone number and it may or may not need to include description of services. Something cute in one area like a picture frame with a heart inside. A friendly feel like something that would be special and feels like yours. I have attached a photo of the existing sign to be replaced.

Thank you for your time.

```html
<!DOCTYPE html>
<html lang="en">
<head>
<meta charset="utf-8">
<title>Gilt Corner — Shop Sign</title>
<link rel="stylesheet" href="https://fonts.googleapis.com/css2?family=Playfair+Display:wght@400&family=Arimo:wght@400&display=swap">
<style>
  :root {
    --backdrop: #e9e7e3;
    --sign-black: #0d0d0d;
    --sign-white: #ffffff;
    --lace-tone: #7b7b7b;
  }
  html, body {
    margin: 0;
    padding: 0;
    width: 1055px;
    height: 1200px;
    overflow: hidden;
    background: var(--backdrop);
  }
  .canvas {
    width: 1055px;
    height: 1200px;
    display: flex;
    align-items: center;
    justify-content: center;
  }
  .shop-sign {
    display: block;
    width: 1000px;
    height: 300px;
  }
  .sign-board { fill: var(--sign-black); }
  .frame-line {
    fill: none;
    stroke: var(--sign-white);
    stroke-width: 2;
  }
  .lace-band {
    fill: none;
    stroke: var(--lace-tone);
    stroke-width: 12;
  }
  .brand-title {
    font-family: "Playfair Display", "Times New Roman", serif;
    font-weight: 400;
    font-size: 118px;
    fill: var(--sign-white);
  }
  .contact-text {
    font-family: "Arimo", Arial, sans-serif;
    font-weight: 400;
    fill: var(--sign-white);
  }
  .contact-phone { font-size: 31px; }
  .contact-web { font-size: 24px; }
  .mark-circle {
    fill: none;
    stroke: var(--sign-white);
    stroke-width: 2;
  }
  .mark-name {
    font-family: "Playfair Display", "Times New Roman", serif;
    font-weight: 400;
    font-size: 22px;
    fill: var(--sign-white);
  }
</style>
</head>
<body>
<main class="canvas">
  <svg class="shop-sign" viewBox="0 0 1000 300" role="img" aria-label="Gilt Corner shop sign">
    <rect class="sign-board" x="0" y="0" width="1000" height="300"/>

    <!-- picture-frame border -->
    <rect class="frame-line" x="10" y="10" width="980" height="280"/>
    <rect class="frame-line" x="15" y="15" width="970" height="270"/>
    <rect class="lace-band" x="25" y="25" width="950" height="250" role="img" aria-label="Scalloped lace border pattern"/>
    <rect class="frame-line" x="36" y="36" width="928" height="228"/>
    <rect class="frame-line" x="41" y="41" width="918" height="218"/>

    <!-- brand mark -->
    <g class="brand-mark">
      <circle class="mark-circle" cx="145" cy="150" r="62"/>
      <text class="mark-name" x="145" y="157" text-anchor="middle">Gilt Corner</text>
    </g>

    <!-- name and contact -->
    <text class="brand-title" x="242" y="176" textLength="668" lengthAdjust="spacingAndGlyphs">GILT CORNER</text>
    <text class="contact-text contact-phone" x="910" y="222" text-anchor="end">T: 01632 960418</text>
    <text class="contact-text contact-web" x="244" y="246">www.giltcorner.co.uk</text>
  </svg>
</main>
</body>
</html>
```